business stationery

have a gorgeous logo that needs to be incorporated on stationery. Was hoping to do something on letterhead that was a paper that looked like "bark" from a tree or something that resembled the "woods." Soft paper with some very basic natural elements. Same thing for business cards. Think American lakeside cabin. Organic. Natural. Calm and welcoming but clear to read and understand. Wanted to use alot of black.

Target Market(s)

buyers of Tobias Wrenfield home. Client that would have more than one home and in need of rare pieces and items to furnish an upmarket lakeside holiday cabin in the woods. Someone who treasures beautiful hand made items, organic foods and a real crackling fire but with money to burn in it!

Industry/Entity Type

Business

Requirements
Must have
• My logo
My business name
www.fernandcopper.example
Natural almost raw effect paper
My ABN: 62 307 514 928 (to be placed in small writing at the bottom of card/letterhead)
Nice to have
• The website will consist of a cabin door that you "open" with a creak sound effect and then you go "inside" to look at the various rooms to start shopping. Want to bring that element of texture and warmth into the stationary also.
Should not have
• Anything modern or hard to read items

```html
<!DOCTYPE html>
<html lang="en">
<head>
<meta charset="utf-8">
<title>Fern &amp; Copper — Stationery</title>
<link rel="stylesheet" href="https://fonts.googleapis.com/css2?family=Crimson+Text:wght@400;700&display=swap">
<style>
  :root {
    --backdrop: #2b150c;
    --paper-light: #efe7db;
    --paper-mid: #e6dccd;
    --paper-shade: #d9ccb9;
    --grain: rgba(196, 180, 158, 0.35);
    --ink: #1c1a18;
    --ink-soft: #3a3632;
    --maple-red: #8a1e1e;
    --shadow: rgba(0, 0, 0, 0.45);
  }
  * { box-sizing: border-box; margin: 0; padding: 0; }
  html, body {
    width: 1200px;
    height: 900px;
    overflow: hidden;
    background: var(--backdrop);
  }
  .stage {
    position: relative;
    width: 1200px;
    height: 900px;
    font-family: "Crimson Text", Georgia, serif;
    color: var(--ink-soft);
  }

  .sheet {
    position: absolute;
    overflow: hidden;
    box-shadow: 0 6px 18px var(--shadow);
  }
  .paper-grain {
    position: absolute;
    inset: 0;
    background:
      radial-gradient(ellipse 8% 4% at 19% 85%, rgba(200,188,170,0.6), transparent 100%),
      radial-gradient(ellipse 8% 4% at 51% 85%, rgba(200,188,170,0.6), transparent 100%),
      radial-gradient(ellipse 18% 70% at 72% 40%, var(--grain), transparent 70%),
      radial-gradient(ellipse 30% 45% at 30% 50%, rgba(255,255,255,0.35), transparent 70%),
      radial-gradient(ellipse 12% 80% at 92% 55%, var(--grain), transparent 70%),
      linear-gradient(95deg, var(--paper-light), var(--paper-mid) 55%, var(--paper-shade));
  }

  .brand-block { position: absolute; }
  .brand-name {
    display: block;
    font-weight: 700;
    color: var(--ink);
    letter-spacing: 0.03em;
    line-height: 1;
    white-space: nowrap;
  }
  .brand-byline {
    display: block;
    text-align: right;
    font-size: 6px;
    letter-spacing: 0.06em;
    text-transform: uppercase;
    color: var(--maple-red);
    margin-top: 3px;
    white-space: nowrap;
  }

  .contact {
    position: absolute;
    font-style: normal;
    font-size: 11px;
    line-height: 13.5px;
    white-space: nowrap;
  }
  .contact .web { margin-bottom: 11px; }
  .contact .abn {
    font-size: 6.5px;
    letter-spacing: 0.04em;
    margin-top: 8px;
  }

  /* Letterhead */
  .letterhead { left: 181px; top: 83px; width: 532px; height: 749px; }
  .letterhead .brand-block { left: 33px; top: 86px; width: 218px; }
  .letterhead .brand-name { font-size: 28px; }
  .letterhead .contact { left: 33px; top: 129px; }

  /* Business cards */
  .card { width: 266px; height: 162px; left: 776px; }
  .card-front { top: 235px; }
  .card-back { top: 412px; }

  .card-front .brand-block { left: 42px; top: 82px; width: 182px; }
  .card-front .brand-name { font-size: 23px; text-align: center; }

  .card-back .contact { left: 23px; top: 50px; font-size: 10px; line-height: 12.5px; }
  .card-back .contact .abn { font-size: 5.5px; margin-top: 10px; }

  .card-back .brand-block { left: 160px; top: 66px; width: 92px; }
  .card-back .brand-name {
    font-size: 17px;
    line-height: 1.1;
    text-align: center;
    white-space: normal;
  }
</style>
</head>
<body>
<main class="stage">

  <section class="sheet letterhead" aria-label="Letterhead">
    <div class="paper-grain" role="img" aria-label="Pale natural wood-grain paper texture with two small knots"></div>
    <div class="brand-block">
      <span class="brand-name">FERN &amp; COPPER</span>
      <span class="brand-byline">by Odette Harlow</span>
    </div>
    <address class="contact">
      <p class="web">www.fernandcopper.example</p>
      <p>4870 W. Birchwood Ln.</p>
      <p>Lakemont, IN 46290-3314</p>
      <p>555/214-8830</p>
      <p class="abn">ABN 62 307 514 928</p>
    </address>
  </section>

  <section class="sheet card card-front" aria-label="Business card front">
    <div class="paper-grain" role="img" aria-label="Pale natural wood-grain paper texture"></div>
    <div class="brand-block">
      <span class="brand-name">FERN &amp; COPPER</span>
      <span class="brand-byline">by Odette Harlow</span>
    </div>
  </section>

  <section class="sheet card card-back" aria-label="Business card back">
    <div class="paper-grain" role="img" aria-label="Pale natural wood-grain paper texture"></div>
    <address class="contact">
      <p>4870 W. Birchwood Ln.</p>
      <p>Lakemont, IN 46290-3314</p>
      <p class="web">555/214-8830</p>
      <p>www.fernandcopper.example</p>
      <p class="abn">ABN 62 307 514 928</p>
    </address>
    <div class="brand-block">
      <span class="brand-name">FERN &amp; COPPER</span>
    </div>
  </section>

</main>
</body>
</html>
```